Brochure Redesign

We need a new, adapted, design for our Brochure. A few weeks ago we've setup a new Homepage design and for now we want to adapt our old Brochure to the new design.

Requirements:
-) Place the 3 products quite prominent
-) Place also our add ons
-) Use the Keyvisuals you can find on the Homepage

New Homepage: www.rufwerkstatt.at
Old Folder version - see attached

Requirements
Must have
• Logo and basic design from Homepage

```html
<!DOCTYPE html>
<html lang="de">
<head>
<meta charset="utf-8">
<title>Rufwerkstatt Folder – Innenseite</title>
<link href="https://fonts.googleapis.com/css2?family=Arimo:ital,wght@0,400;0,700;1,400&display=swap" rel="stylesheet">
<style>
  :root{
    --wine:#6b0a0a;
    --orange:#f08a00;
    --yellow:#f9c800;
    --yellow-light:#fde24a;
    --grey-box:#e4e4e4;
    --text-grey:#444;
    --mark:#999;
    --white:#fff;
  }
  *{margin:0;padding:0;box-sizing:border-box}
  html,body{width:1200px;height:960px;overflow:hidden;background:var(--white)}
  body{font-family:"Arimo",Arial,sans-serif;color:var(--text-grey)}
  .sheet{position:relative;width:1200px;height:960px}
  .shapes{position:absolute;left:0;top:0}
  .abs{position:absolute}

  /* left panel */
  .benefits-title{left:132px;top:160px;color:var(--white);font-size:26px;font-weight:700;line-height:1}
  .benefits-sub{left:132px;top:190px;color:var(--white);font-size:16px;font-weight:700}
  .benefits-list{left:132px;top:216px;list-style:none;color:var(--white);font-size:13px}
  .benefits-list li{display:flex;align-items:center;height:21px}
  .benefits-list svg{margin-right:8px;flex:none}

  .step-label{font-size:11px;font-weight:700;color:var(--wine);text-align:right;width:130px}
  .step-num{color:var(--white);font-size:27px;font-weight:700;width:34px;text-align:center}
  .step-text{font-size:9.6px;line-height:1.4;text-align:right;width:214px;color:var(--text-grey);white-space:nowrap}

  /* middle panel */
  .app-title{left:508px;top:170px;font-size:13px;font-weight:700;color:var(--wine)}
  .app-text{left:508px;top:188px;font-size:9px;line-height:1.3;color:var(--wine);white-space:nowrap}
  .test-title{left:457px;top:338px;font-size:16px;font-weight:700;color:var(--wine)}
  .test-text{left:457px;top:364px;font-size:10.5px;line-height:1.48;color:var(--wine);white-space:nowrap}
  .test-text p+p{margin-top:15px}
  .contact-title{left:457px;top:500px;font-size:20px;font-weight:700;color:var(--wine)}
  .contact-claim{left:457px;top:528px;font-size:15.5px;color:var(--text-grey)}
  .contact-list{left:457px;top:608px;font-size:10.5px;line-height:1.6;color:var(--text-grey)}
  .contact-list dt{font-weight:700;color:#222}
  .contact-name{left:472px;top:807px;font-size:11px;color:var(--text-grey)}

  /* right panel */
  .addons-head{left:768px;top:112px;width:360px;height:54px;line-height:54px;text-align:center;color:var(--white);font-size:17px;font-weight:700}
  .price{background:var(--yellow-light);border-radius:4px;color:var(--wine);font-weight:700;text-align:center}
  .price-main{left:903px;width:68px;height:28px;line-height:28px;font-size:13px}
  .addon-title{left:768px;width:360px;text-align:center;font-size:14px;font-weight:700;color:var(--wine)}
  .addon-text{left:768px;width:360px;text-align:center;font-size:9px;line-height:1.3;color:var(--text-grey);white-space:nowrap}
  .price-small{top:700px;width:68px;height:34px;padding-top:3px}
  .price-small span{display:block;font-size:6.5px;line-height:1.2}
  .price-small b{display:block;font-size:13px;line-height:1.3}
  .addon-note{left:768px;width:360px;top:808px;text-align:center;font-size:8px;font-style:italic;color:#777}
</style>
</head>
<body>
<div class="sheet">

<svg class="shapes" width="1200" height="960" viewBox="0 0 1200 960">
  <defs>
    <linearGradient id="midGrad" x1="0" y1="0" x2="0" y2="1">
      <stop offset="0" stop-color="#fbd000"/>
      <stop offset="1" stop-color="#f3a600"/>
    </linearGradient>
    <linearGradient id="bubbleGrad" x1="0" y1="0" x2="0" y2="1">
      <stop offset="0" stop-color="#f9a11b"/>
      <stop offset="1" stop-color="#ec7a00"/>
    </linearGradient>
    <linearGradient id="suitGrad" x1="0" y1="0" x2="0" y2="1">
      <stop offset="0" stop-color="#e8c87a"/>
      <stop offset="0.25" stop-color="#d9b9a2"/>
      <stop offset="0.4" stop-color="#2a2a2e"/>
      <stop offset="1" stop-color="#111114"/>
    </linearGradient>
  </defs>

  <!-- crop marks -->
  <g stroke="var(--mark)" stroke-width="1" fill="none">
    <path d="M96,96 V122 M70,112 H88"/>
    <path d="M1104,96 V122 M1112,112 H1130"/>
    <path d="M96,838 V862 M70,838 H88"/>
    <path d="M1104,838 V862 M1112,838 H1130"/>
    <path d="M431,96 V104 M431,110 V118 M768,96 V104 M768,110 V118" stroke-dasharray="2 2"/>
    <path d="M431,842 V850 M431,856 V864 M768,842 V850 M768,856 V864" stroke-dasharray="2 2"/>
  </g>

  <!-- left panel swoosh -->
  <path d="M84,112 H430 V232 C370,300 250,350 84,372 Z" fill="var(--wine)"/>
  <path d="M84,372 C250,350 370,300 430,232 V250 C360,340 230,400 84,424 Z" fill="var(--orange)"/>

  <!-- middle panel -->
  <path d="M431,300 C520,270 560,150 650,112 H768 V484 H431 Z" fill="url(#midGrad)"/>
  <path d="M431,300 C520,270 560,150 650,112 H700 C610,140 560,260 431,330 Z" fill="var(--orange)"/>

  <!-- speech bubble -->
  <path d="M482,132 H638 Q648,132 646,142 L636,252 Q635,262 625,262 H530 L502,290 L508,262 H490 Q480,262 480,252 L472,142 Q472,132 482,132 Z" fill="url(#bubbleGrad)" stroke="var(--wine)" stroke-width="2.5"/>

  <!-- phone -->
  <rect x="654" y="214" width="72" height="108" rx="10" fill="#d2d2d2" role="img" aria-label="Smartphone mit geöffneter App"/>

  <!-- store badges as plain shapes -->
  <rect x="480" y="280" width="98" height="32" rx="5" fill="#111"/>
  <rect x="592" y="280" width="34" height="34" rx="4" fill="#8cc63e"/>

  <!-- contact person -->
  <rect x="612" y="562" width="122" height="284" fill="url(#suitGrad)" role="img" aria-label="Porträt der Ansprechpartnerin im dunklen Blazer"/>
  <rect x="522" y="758" width="82" height="42" fill="#efefef" role="img" aria-label="Unterschrift der Ansprechpartnerin"/>

  <!-- steps -->
  <g>
    <rect x="126" y="430" width="280" height="66" fill="var(--grey-box)"/>
    <path d="M126,412 H160 V496 H138 Q126,496 126,484 Z" fill="var(--wine)"/>
    <path d="M272,412 H406 V430 H266 Z" fill="var(--yellow)"/>
    <circle cx="162" cy="412" r="36" fill="#f1e6de" stroke="#fff" stroke-width="2" role="img" aria-label="Hände auf einer Tastatur"/>
  </g>
  <g>
    <rect x="126" y="570" width="280" height="66" fill="var(--grey-box)"/>
    <path d="M126,552 H160 V636 H138 Q126,636 126,624 Z" fill="var(--wine)"/>
    <path d="M272,552 H406 V570 H266 Z" fill="var(--yellow)"/>
    <circle cx="158" cy="552" r="34" fill="#e9e4e0" stroke="#fff" stroke-width="2" role="img" aria-label="Hand an einer Telefontastatur"/>
  </g>
  <g>
    <rect x="126" y="712" width="280" height="66" fill="var(--grey-box)"/>
    <path d="M126,694 H160 V778 H138 Q126,778 126,766 Z" fill="var(--wine)"/>
    <path d="M272,694 H406 V712 H266 Z" fill="var(--yellow)"/>
    <circle cx="162" cy="694" r="36" fill="#ead9cc" stroke="#fff" stroke-width="2" role="img" aria-label="Mitarbeiterin mit Headset"/>
  </g>

  <!-- right panel -->
  <rect x="768" y="112" width="360" height="54" fill="var(--wine)"/>
  <circle cx="936" cy="222" r="40" fill="#e8e8e8" role="img" aria-label="Bücherstapel mit Computermaus"/>
  <circle cx="936" cy="438" r="40" fill="#e8e8e8" role="img" aria-label="Kalenderblatt"/>
  <circle cx="936" cy="648" r="40" fill="#e8e8e8" role="img" aria-label="Telefonanlage und Headset"/>
</svg>

<!-- left panel -->
<h2 class="abs benefits-title">Ihre Vorteile</h2>
<p class="abs benefits-sub">Einfach, Immer, Erreichbar</p>
<ul class="abs benefits-list">
  <li><svg width="13" height="13" viewBox="0 0 13 13"><circle cx="6.5" cy="6.5" r="6.5" fill="var(--yellow)"/><path d="M3.5,6.8 L5.8,9 L9.6,4.3" stroke="var(--wine)" stroke-width="1.8" fill="none"/></svg>Individueller Meldetext</li>
  <li><svg width="13" height="13" viewBox="0 0 13 13"><circle cx="6.5" cy="6.5" r="6.5" fill="var(--yellow)"/><path d="M3.5,6.8 L5.8,9 L9.6,4.3" stroke="var(--wine)" stroke-width="1.8" fill="none"/></svg>Beliebig viele Mitarbeiter</li>
  <li><svg width="13" height="13" viewBox="0 0 13 13"><circle cx="6.5" cy="6.5" r="6.5" fill="var(--yellow)"/><path d="M3.5,6.8 L5.8,9 L9.6,4.3" stroke="var(--wine)" stroke-width="1.8" fill="none"/></svg>24h Erreichbarkeit</li>
  <li><svg width="13" height="13" viewBox="0 0 13 13"><circle cx="6.5" cy="6.5" r="6.5" fill="var(--yellow)"/><path d="M3.5,6.8 L5.8,9 L9.6,4.3" stroke="var(--wine)" stroke-width="1.8" fill="none"/></svg>Ohne Mindestvertragslaufzeit</li>
  <li><svg width="13" height="13" viewBox="0 0 13 13"><circle cx="6.5" cy="6.5" r="6.5" fill="var(--yellow)"/><path d="M3.5,6.8 L5.8,9 L9.6,4.3" stroke="var(--wine)" stroke-width="1.8" fill="none"/></svg>Keine versteckten Callminuten</li>
</ul>

<div class="abs step-label" style="left:270px;top:415px">Dateneingabe</div>
<div class="abs step-num" style="left:126px;top:452px">1</div>
<p class="abs step-text" style="left:184px;top:442px">Sie können Ihr neues Sekretariat in nur wenigen<br>Minuten ganz einfach online einrichten. Geben<br>Sie alle relevanten Daten menügeführt ein.</p>

<div class="abs step-label" style="left:270px;top:555px">Rufumleitung</div>
<div class="abs step-num" style="left:126px;top:592px">2</div>
<p class="abs step-text" style="left:184px;top:585px">Sofort nach erfolgreicher Buchung erhalten Sie<br>Ihre Zielrufnummer. Leiten Sie Ihr Telefon einfach<br>auf diese Nummer um diese Nummer um.</p>

<div class="abs step-label" style="left:270px;top:697px">Ihr Sekretariat</div>
<div class="abs step-num" style="left:126px;top:734px">3</div>
<p class="abs step-text" style="left:184px;top:724px">Ihr neues Sekretariat ist nun aktiv. Sie und all Ihre<br>Mitarbeiter werden in Echtzeit, individuell über<br>eingehende Anrufe informiert.</p>

<!-- middle panel -->
<h3 class="abs app-title">Kostenlose App</h3>
<p class="abs app-text">Laden Sie jetzt die<br>kostenlose rufwerkstatt<br>App direkt online herunter.</p>

<h3 class="abs test-title">24h - GRATIS - TEST</h3>
<div class="abs test-text">
  <p>Wählen Sie Ihren persönlichen Meldetext und testen<br>Sie uns 24 Stunden vollkommen kostenlos<br>und unverbindlich.</p>
  <p>Wenn wir Sie überzeugt haben, können Sie in Ihrem<br>Kundenbereich alle weiteren<br>Daten ergänzen und Ihr neues Sekretariat fix buchen.</p>
</div>

<h2 class="abs contact-title">Ihr Ansprechpartner</h2>
<p class="abs contact-claim">Praxisnah. Kompetent. Engagiert.</p>
<dl class="abs contact-list">
  <dt>Freeline</dt><dd>0800 / 0600 42</dd>
  <dt>Email</dt><dd>vertrieb@rufwerkstatt.at</dd>
  <dt>Web</dt><dd>www.rufwerkstatt.at</dd>
</dl>
<p class="abs contact-name">Frau Prok. Selma Auer</p>

<!-- right panel -->
<h2 class="abs addons-head">ADD ON'S</h2>

<div class="abs price price-main" style="top:272px">€ 19,-</div>
<h3 class="abs addon-title" style="top:306px">Online Wissensdatenbank</h3>
<p class="abs addon-text" style="top:328px">Bietet die Grundlage für die professionelle Sammlung<br>Ihrer Informationen. Strukturierte Informations-<br>aufbereitung ermöglicht Suchanfragen.<br>(Setup einmalig € 99,-)</p>

<div class="abs price price-main" style="top:488px">€ 29,-</div>
<h3 class="abs addon-title" style="top:520px">Online Terminkalender</h3>
<p class="abs addon-text" style="top:542px">Sämtliche Anforderungen wie Terminlängen, Kategorien,<br>etc. werden individuell an Ihre Bedürfnisse angepasst<br>und ermöglichen ortsunabhängig alle Termine zu verwalten.<br>(Setup einmalig € 199,-)</p>

<div class="abs price price-small" style="left:816px"><span>Neutral</span><b>€ 4,90</b></div>
<div class="abs price price-small" style="left:902px"><span>Personalisiert</span><b>€ 7,90</b></div>
<div class="abs price price-small" style="left:988px"><span>Anrufbeantworter</span><b>€ 9,90</b></div>
<h3 class="abs addon-title" style="top:742px">Tonbänder &amp; Co</h3>
<p class="abs addon-text" style="top:762px">Sie haben die Möglichkeit mit neutralen und individuellen<br>Bandansagen oder einer Anrufbeantworterfunktion Ihren<br>Kunden noch mehr Service zu bieten.</p>
<p class="abs addon-note">Die angeführten Add On Preise gelten monatlich.</p>

</div>
</body>
</html>
```